Upmarket building and construction company needs signage

Our building company R Voss Construction, needs signage to put up on the side of our vehicle trailers and on site fencing. We are a building company that specialises in residential construction and carpentry .

I will attach our logo and some inspirational pics for site fencing as well as what our trailer looks like .
Other details i would like on the sign are our
( email) rvossconstruction@mailpost.example
(mobile ) 0482 913 640
(website ) rvossconstruction. example.au

Target Market(s)

Home owners looking for a reliable local builder who produces good quality work. I have attached some inspirational pics.

Industry/Entity Type

Building and Construction

Colors

Designer to choose colors to be used in the design.

Requirements
Must have
• Our logo, contact information
Nice to have
• We would like the design to have elements of being Elegant, Serious, Modern, Professional, Masculine, Conservative and Upmarket.

```html
<!DOCTYPE html>
<html lang="en">
<head>
<meta charset="utf-8">
<title>R Voss Construction – Signage</title>
<link href="https://fonts.googleapis.com/css2?family=Jost:wght@300&family=Montserrat:wght@600&display=swap" rel="stylesheet">
<style>
  :root{
    --page:#f4f4f4;
    --panel-light:#f2f2f2;
    --panel-white:#ffffff;
    --swoosh-grey:#8a8a8a;
    --band:#474747;
    --accent:#e2a31b;
    --logo-ink:#5a5a5a;
    --contact-ink:#ffffff;
  }
  html,body{margin:0;padding:0;}
  body{
    width:1200px;height:3427px;overflow:hidden;
    background:var(--page);
    display:flex;flex-direction:column;align-items:center;justify-content:space-around;
  }
  .sign{display:block;box-shadow:0 2px 10px rgba(0,0,0,.12);}
  .logo-name{font-family:"Jost",sans-serif;font-weight:300;fill:var(--logo-ink);}
  .logo-tagline{font-family:"Jost",sans-serif;font-weight:300;fill:var(--logo-ink);letter-spacing:1px;}
  .contact-line{font-family:"Montserrat",sans-serif;font-weight:600;fill:var(--contact-ink);}
</style>
</head>
<body>

<svg width="0" height="0" style="position:absolute" aria-hidden="true">
  <defs>
    <linearGradient id="light-field" x1="0" y1="0" x2="1" y2="1">
      <stop offset="0" stop-color="#e9e9e9"/>
      <stop offset="0.5" stop-color="#ffffff"/>
      <stop offset="1" stop-color="#f1f1f1"/>
    </linearGradient>
    <linearGradient id="dark-field" x1="0" y1="0" x2="0" y2="1">
      <stop offset="0" stop-color="#878787"/>
      <stop offset="1" stop-color="#4c4c4c"/>
    </linearGradient>
    <symbol id="wide-art" viewBox="0 0 1100 500">
      <rect width="1100" height="500" fill="url(#light-field)"/>
      <path d="M0 430 C600 430 880 300 960 0 L1100 0 L1100 500 L0 500 Z" fill="url(#dark-field)"/>
      <path d="M640 352 C800 292 885 175 918 0 L938 0 C900 185 812 315 640 352 Z" fill="var(--swoosh-grey)"/>
      <path d="M640 382 C825 332 930 195 975 0 L1005 0 C955 205 845 345 640 382 Z" fill="var(--panel-white)"/>
      <path d="M0 404 C300 420 490 402 645 345 C495 392 300 406 0 388 Z" fill="var(--accent)"/>
      <rect x="0" y="432" width="1100" height="68" fill="var(--band)"/>
    </symbol>
  </defs>
</svg>

<!-- Site fencing banner -->
<svg class="sign sign--fence" width="1100" height="500" viewBox="0 0 1100 500">
  <use href="#wide-art" width="1100" height="500"/>
  <text class="logo-name" x="135" y="210" font-size="92">R VOSS</text>
  <text class="logo-name" x="137" y="276" font-size="50">CONSTRUCTION</text>
  <text class="logo-tagline" x="139" y="316" font-size="25">BUILDING AND CARPENTRY</text>
  <text class="contact-line" x="30" y="475" font-size="25" textLength="1040" lengthAdjust="spacingAndGlyphs">rvossconstruction@mailpost.example | 0482 913 640 | rvossconstruction. example.au</text>
</svg>

<!-- Box body header panel -->
<svg class="sign sign--header" width="380" height="170" viewBox="0 0 380 170">
  <rect width="380" height="170" fill="var(--panel-light)"/>
  <text class="logo-name" x="190" y="78" font-size="46" text-anchor="middle">R VOSS</text>
  <text class="logo-name" x="190" y="112" font-size="25" text-anchor="middle">CONSTRUCTION</text>
  <text class="logo-tagline" x="190" y="134" font-size="12" text-anchor="middle">BUILDING AND CARPENTRY</text>
</svg>

<!-- Trailer side, right-hand -->
<svg class="sign sign--side" width="1000" height="455" viewBox="0 0 1100 500">
  <use href="#wide-art" width="1100" height="500"/>
  <text class="logo-name" x="260" y="210" font-size="86">R VOSS</text>
  <text class="logo-name" x="262" y="272" font-size="46">CONSTRUCTION</text>
  <text class="logo-tagline" x="264" y="308" font-size="23">BUILDING AND CARPENTRY</text>
  <text class="contact-line" x="40" y="475" font-size="26" textLength="1020" lengthAdjust="spacingAndGlyphs">rvossconstruction@mailpost.example | 0482 913 640 | rvossconstruction. example.au</text>
</svg>

<!-- Rear doors -->
<svg class="sign sign--rear" width="400" height="440" viewBox="0 0 400 440">
  <rect width="400" height="440" fill="url(#light-field)"/>
  <path d="M0 350 C220 350 360 255 400 120 L400 440 L0 440 Z" fill="url(#dark-field)"/>
  <path d="M225 334 C320 305 380 225 400 160 L400 182 C376 248 322 312 225 334 Z" fill="var(--swoosh-grey)"/>
  <path d="M225 350 C330 325 385 255 400 205 L400 232 C380 285 322 340 225 350 Z" fill="var(--panel-white)"/>
  <path d="M0 336 C110 344 180 340 232 326 C180 338 110 340 0 327 Z" fill="var(--accent)"/>
  <rect x="0" y="376" width="400" height="64" fill="var(--band)"/>
  <text class="logo-name" x="60" y="180" font-size="54">R VOSS</text>
  <text class="logo-name" x="61" y="218" font-size="29">CONSTRUCTION</text>
  <text class="logo-tagline" x="62" y="242" font-size="14">BUILDING AND CARPENTRY</text>
  <text class="contact-line" x="12" y="412" font-size="9.5" textLength="376" lengthAdjust="spacingAndGlyphs">rvossconstruction@mailpost.example | 0482 913 640 | rvossconstruction. example.au</text>
</svg>

<!-- Trailer side, left-hand -->
<svg class="sign sign--side-left" width="1000" height="455" viewBox="0 0 1100 500">
  <use href="#wide-art" width="1100" height="500" transform="translate(1100 0) scale(-1 1)"/>
  <text class="logo-name" x="500" y="210" font-size="86">R VOSS</text>
  <text class="logo-name" x="502" y="272" font-size="46">CONSTRUCTION</text>
  <text class="logo-tagline" x="504" y="308" font-size="23">BUILDING AND CARPENTRY</text>
  <text class="contact-line" x="40" y="475" font-size="26" textLength="1020" lengthAdjust="spacingAndGlyphs">rvossconstruction@mailpost.example | 0482 913 640 | rvossconstruction. example.au</text>
</svg>

</body>
</html>
```